High End Notary Service Business Card Design

Want a professional and elegant/luxurious business card that is clean and simple in the design. A notary is a trusted professional that helps people sign very important documents. The card should be in alignment with this service provided.

Most of the time, service will be for the purchase of a home or refinance of a mortgage

There is NO LOGO. This is aesthetic. A look and feel. Conveying professionalism and concierge level of service.

Target Market(s)

Other business professionals, Lawyers, Escrow Officers, Loan Officers

Industry/Entity Type

Legal

Contact Information for Business Card

This will be a one-sided business card

Colors
35a7d7
3176b5
85cae6
d3a5cc
b868aa
ffffff
0356a4

Requirements
Must have
• Lorena T. Mirabel-Hodgkins
Notary Public

642-871-3094
MirabelSigningDesk@Wexmail.com
Nice to have
• Headshot photo below. Convey the aspect of signing documents. No black cards. Preference is shades of blue: light blue, navy, aqua, gold, white, or lavendar, etc.
Should not have
• No scales or legal scales.

```html
<!DOCTYPE html>
<html lang="en">
<head>
<meta charset="utf-8">
<title>Lorena T. Mirabel-Hodgkins — Notary Public Business Card</title>
<link rel="stylesheet" href="https://fonts.googleapis.com/css2?family=Cinzel:wght@600;700&family=Open+Sans:wght@400&display=swap">
<style>
  :root {
    --page-bg: #e8e8e8;
    --card-blue: #1b63ad;
    --accent-gold: #f6c126;
    --accent-gold-deep: #c9a036;
    --portrait-tone-top: #a9aec0;
    --portrait-tone-bottom: #9ea4b8;
    --text-white: #ffffff;
  }
  * { margin: 0; padding: 0; box-sizing: border-box; }
  html, body {
    width: 1200px;
    height: 800px;
    overflow: hidden;
    background: var(--page-bg);
  }
  .business-card {
    position: absolute;
    left: 75px;
    top: 100px;
    width: 1050px;
    height: 600px;
    background: var(--card-blue);
    overflow: hidden;
  }
  .card-artwork {
    position: absolute;
    inset: 0;
    width: 1050px;
    height: 600px;
  }
  .identity {
    position: absolute;
    left: 610px;
    top: 138px;
    width: 380px;
    text-align: center;
  }
  .identity__name {
    font-family: "Cinzel", serif;
    font-weight: 700;
    font-size: 27px;
    letter-spacing: 0.2px;
    color: var(--text-white);
    white-space: nowrap;
    line-height: 1.1;
  }
  .identity__rule {
    width: 372px;
    height: 2px;
    margin: 4px auto 3px;
    background: var(--accent-gold);
  }
  .identity__title {
    font-family: "Cinzel", serif;
    font-weight: 700;
    font-size: 27px;
    color: var(--accent-gold);
    line-height: 1.1;
  }
  .contact-list {
    position: absolute;
    left: 590px;
    top: 472px;
    list-style: none;
  }
  .contact-list__item {
    display: flex;
    align-items: center;
    height: 42px;
    margin-bottom: 10px;
    font-family: "Open Sans", sans-serif;
    font-size: 22px;
    color: var(--text-white);
  }
  .contact-list__icon {
    width: 42px;
    height: 42px;
    margin-right: 4px;
    flex: none;
  }
</style>
</head>
<body>
  <article class="business-card">
    <svg class="card-artwork" viewBox="0 0 1050 600" aria-hidden="false">
      <defs>
        <linearGradient id="portraitTone" x1="0" y1="0" x2="0" y2="1">
          <stop offset="0" stop-color="var(--portrait-tone-top)"/>
          <stop offset="1" stop-color="var(--portrait-tone-bottom)"/>
        </linearGradient>
      </defs>
      <path class="portrait-area" role="img" aria-label="Headshot photo of the notary, smiling, against a soft grey backdrop"
            d="M0,0 L449,0 C600,140 590,420 365,600 L0,600 Z" fill="url(#portraitTone)"/>
      <path class="gold-swoosh" d="M449,0 L472,0 C620,160 610,420 458,600 L365,600 C590,420 600,140 449,0 Z" fill="var(--accent-gold)"/>
      <path class="gold-swoosh-shade" d="M560,340 C548,450 478,540 402,600 L458,600 C532,520 572,440 580,350 Z" fill="var(--accent-gold-deep)"/>
    </svg>

    <header class="identity">
      <h1 class="identity__name">Lorena T. Mirabel-Hodgkins</h1>
      <div class="identity__rule"></div>
      <p class="identity__title">Notary Public</p>
    </header>

    <ul class="contact-list">
      <li class="contact-list__item">
        <svg class="contact-list__icon" viewBox="0 0 42 42" aria-hidden="true">
          <circle cx="21" cy="21" r="20" fill="var(--accent-gold)"/>
          <path d="M16,10 l4,0 l2,6 l-3,2.5 c1.5,3.5 3.5,5.5 6.5,7 l2.5,-3 l6,2 l0,4 c0,2 -1.5,3 -3,3 c-9,-1 -16,-8 -17,-17 c0,-1.5 1,-4.5 2,-4.5 z" fill="var(--card-blue)"/>
        </svg>
        <span>642-871-3094</span>
      </li>
      <li class="contact-list__item">
        <svg class="contact-list__icon" viewBox="0 0 42 42" aria-hidden="true">
          <circle cx="21" cy="21" r="20" fill="var(--accent-gold)"/>
          <rect x="11" y="14" width="20" height="14" rx="1.5" fill="var(--card-blue)"/>
          <path d="M12,15 L21,22 L30,15" fill="none" stroke="var(--accent-gold)" stroke-width="2"/>
        </svg>
        <span>MirabelSigningDesk@Wexmail.com</span>
      </li>
    </ul>
  </article>
</body>
</html>
```